Letter and Envelope Design For Larchmont Realty

Please design a letter and an envelope incorporating our logo (See Attached). We are also launched a business card contest. Since we want them to match, please feel free to submit a design for both the business card and also the letter design and envelope.

Requirements
Must have
• The envelope, the letter and the business cards must match somehow connecting the designs. We want them to have something that holds them together besides the logo.

```html
<!DOCTYPE html>
<html lang="en">
<head>
<meta charset="utf-8">
<title>Larchmont Realty Envelope</title>
<link href="https://fonts.googleapis.com/css2?family=Questrial&display=swap" rel="stylesheet">
<style>
  :root {
    --navy: #172c74;
    --ink: #555555;
    --edge: #c6c6c6;
    --paper: #ffffff;
  }
  html, body {
    margin: 0;
    padding: 0;
    width: 1200px;
    height: 554px;
    overflow: hidden;
    background: var(--paper);
    font-family: "Questrial", "Century Gothic", sans-serif;
  }
  .canvas {
    position: relative;
    width: 1200px;
    height: 554px;
  }
  .envelope {
    position: absolute;
    left: 37px;
    top: 33px;
    width: 1125px;
    height: 489px;
    border: 1px solid var(--edge);
    background: var(--paper);
    overflow: hidden;
  }
  .sender {
    position: absolute;
    left: 53px;
    top: 0;
    width: 176px;
    text-align: center;
  }
  .brand-mark {
    display: block;
    margin: 42px auto 0;
  }
  .brand-name {
    margin: 8px 0 0;
    color: var(--navy);
    font-size: 19px;
    letter-spacing: 2.4px;
    line-height: 21px;
    font-weight: 400;
  }
  .return-address {
    margin: 18px 0 0;
    color: var(--ink);
    font-size: 13px;
    line-height: 18px;
    font-style: normal;
  }
  .brand-band {
    position: absolute;
    left: 53px;
    top: 255px;
    width: 175px;
    height: 240px;
    background: var(--navy);
  }
</style>
</head>
<body>
  <div class="canvas">
    <div class="envelope">
      <div class="sender">
        <svg class="brand-mark" width="70" height="70" viewBox="0 0 70 70" aria-hidden="true">
          <circle cx="35" cy="35" r="33" fill="none" stroke="var(--navy)" stroke-width="2.5"/>
        </svg>
        <p class="brand-name">LARCHMONT<br>REALTY</p>
        <address class="return-address">
          LARCHMONT REALTY, Inc.<br>
          1417 Alder Avenue<br>
          Brookfield, NJ 07099
        </address>
      </div>
      <div class="brand-band"></div>
    </div>
  </div>
</body>
</html>
```